Tri-fold 8.5x11" brochure for my company's service

I am looking for a brochure design (to be used with Bramwell Mart printing service-- their templates have been included) for my company, Quillstone Scholastics. We host, support, and provide custom programming for the open-source product, Quillstone (which we also created).

I have included a Notes file, which provides more potential copy and points about the company. Please read it thoroughly, but feel free to experiment, edit, only use pieces of text, etc. Don't feel like you have to follow anything in there exactly.

I have included a couple different versions of our logo.

I have also included a zip file of several nice-looking screenshots from our software.

I have also included a zip file of stock photos I have purchased, but feel free to use other ones if you like-- You can use free watermarked versions and I will purchase the full image later and add it in. You also don't have to use the stock photos at all; your choice.

I can make my way around Gimp and Photoshop, so the final product MUST be in a format (with different image and text layers) I can edit myself later for final tweaks. I can work with psd and xcf (gimp) files. If you prefer to work with Illustrator or InDesign, please check google; there are several answers for how to convert to a layered psd file.

Final product must be in 300 DPI, per the printer's instructions. If you have to use lower-res versions of images (like for unpaid stock photos) that's OK as long as you give me the URL to buy to full version; I can place the full size images myself.

Target Market(s)

University / College faculty, registrars, administrators, VP's, presidents, etc.

Industry/Entity Type

Higher Education, Universities, Colleges, Student Success

Font styles to use
Serif
Sans Serif
Other font styles liked:
• MONTSERRAT is the font used in my logo, I use RALEWAY on the website. But these are not requirements-- Use what you think looks best.

Colors

Designer to choose colors to be used in the design.

Requirements
Must have
• The final product MUST be in a format (with different image and text layers) that I can edit myself later for final tweaks. I can work with psd and xcf (gimp) files. 300dpi required by printer. Follow the template files included for exact measurements. If you prefer to work with Illustrator or InDesign, please check google; there are several answers for how to convert to a layered psd file.
Nice to have
• I would like (if possible) to mention that the software, Quillstone is open source. I feel like that is a big selling point for universities. Also, please try to have a similar look and feel as the website: quillstonescholastics.example, if possible. If possible, you can mention that our service runs on state-of-the-art cloud based hardware, though this is not a requirement. Also, try to work in "affordable pricing" and/or "great for schools of all sizes", or similar, if possible. One of our selling points is that we are much less expensive than our competitors.
Should not have
• Big walls of text. I appreciate trying to cram in a lot of information from my notes, but too much and it can look very crowded.

```html
<!DOCTYPE html>
<html lang="en">
<head>
<meta charset="utf-8">
<title>Quillstone Scholastics – Tri-fold Brochure</title>
<link href="https://fonts.googleapis.com/css2?family=Montserrat:wght@400;600;700;800&family=Raleway:wght@400;500;600&display=swap" rel="stylesheet">
<style>
:root{
  --blue:#1e9ad6;
  --blue-dark:#16709f;
  --pink:#e6316f;
  --orange:#f7941e;
  --navy:#263544;
  --ink:#4a5561;
  --paper:#ffffff;
  --stage:#e9eaec;
  --rule:#d9dde2;
}
*{box-sizing:border-box;margin:0;padding:0}
html,body{width:900px;height:1200px;overflow:hidden}
body{background:var(--stage);font-family:"Raleway",sans-serif;color:var(--ink);position:relative}
.spread{position:absolute;left:90px;width:720px;height:556px;background:var(--paper);display:flex;box-shadow:0 4px 14px rgba(0,0,0,.18)}
.spread--outside{top:30px}
.spread--inside{top:614px}
.panel{position:relative;width:240px;height:100%;overflow:hidden;border-right:1px solid #eef0f2}
.panel:last-child{border-right:none}
.stripes{position:absolute;left:0;width:100%;pointer-events:none}
.brand{display:flex;align-items:center;gap:6px;font-family:"Montserrat",sans-serif;font-weight:800;color:var(--navy);text-transform:uppercase;letter-spacing:.5px}
.brand__mark{width:12px;height:12px;background:var(--orange);flex:none}
.photo{position:absolute;display:block}
.body-text{font-size:7.2px;line-height:1.5;color:var(--ink)}
.ticks{list-style:none}
.ticks li{position:relative;padding-left:13px;font-size:7.2px;line-height:1.45;margin-bottom:5px}
.ticks li::before{content:"";position:absolute;left:0;top:1px;width:8px;height:8px;border-radius:50%;background:var(--blue)}
.ticks li::after{content:"";position:absolute;left:2.3px;top:2.6px;width:3px;height:1.8px;border-left:1.2px solid #fff;border-bottom:1.2px solid #fff;transform:rotate(-45deg)}
.heading{font-family:"Montserrat",sans-serif;font-weight:800;text-transform:uppercase;line-height:1.05}

/* Features panel */
.features__band{position:absolute;top:0;left:0;width:100%;height:44px;background:var(--blue)}
.features__title{position:absolute;top:14px;left:18px;font-size:15px;color:#fff}
.features__title span{color:var(--orange)}
.features__intro{position:absolute;top:56px;left:18px;right:16px}
.features__list{position:absolute;top:150px;left:18px;right:16px}

/* Back panel */
.back__brand{position:absolute;top:116px;left:0;width:100%;justify-content:center;font-size:13px}
.back__copy{position:absolute;top:150px;left:22px;right:22px;text-align:center}
.back__call{position:absolute;top:330px;left:0;width:100%;text-align:center;font-family:"Montserrat",sans-serif;font-size:8px;font-weight:600;color:var(--pink);text-transform:uppercase;letter-spacing:1px}
.back__phone{position:absolute;top:344px;left:0;width:100%;text-align:center;font-family:"Montserrat",sans-serif;font-size:19px;font-weight:800;color:var(--navy)}
.back__phone svg{vertical-align:-2px;margin-right:5px}
.back__web{position:absolute;top:372px;left:0;width:100%;text-align:center;font-size:7.5px;font-weight:600;color:var(--blue)}

/* Cover panel */
.cover__brand{position:absolute;top:22px;left:20px;font-size:13px}
.cover__tagline{position:absolute;top:40px;left:39px;font-size:6px;letter-spacing:1.5px;color:var(--ink);text-transform:uppercase;font-weight:600}
.cover__headline{position:absolute;top:350px;left:0;width:100%;text-align:center}
.cover__headline .h1{font-size:17px;color:var(--blue)}
.cover__headline .h2{font-size:27px;color:var(--pink)}
.cover__headline .h3{font-size:13px;color:var(--orange);letter-spacing:.5px}
.cover__bar{position:absolute;bottom:0;left:0;width:100%;height:34px;background:var(--blue);color:#fff;font-size:8px;font-weight:600;text-align:center;line-height:34px;letter-spacing:.5px}

/* Inside left */
.in-left__brand{position:absolute;top:14px;left:16px;font-size:10px}
.in-left__list{position:absolute;top:168px;left:16px;right:14px}
.service__title{position:absolute;top:300px;left:16px;font-size:10px;color:var(--pink)}
.service__sub{position:absolute;top:314px;left:16px;font-size:7px;font-weight:600;color:var(--navy)}
.service__items{position:absolute;top:334px;left:16px;right:14px;list-style:none}
.service__items li{display:flex;gap:8px;margin-bottom:10px}
.service__icon{flex:none;width:18px;height:18px;border-radius:50%}
.service__items strong{display:block;font-family:"Montserrat",sans-serif;font-size:7.5px;color:var(--navy);text-transform:uppercase}

/* Inside middle */
.welcome__title{position:absolute;top:22px;left:18px;font-size:15px;color:var(--blue)}
.welcome__title span{color:var(--pink);display:block}
.welcome__copy{position:absolute;top:70px;left:18px;right:16px}
.welcome__copy p{margin-bottom:7px}
.welcome__list{position:absolute;top:250px;left:18px;right:16px}

/* Inside right */
.in-right__copy{position:absolute;top:24px;left:18px;right:16px}
.in-right__copy p{margin-bottom:7px}
.in-right__list{position:absolute;top:268px;left:18px;right:16px}
</style>
</head>
<body>

<!-- OUTSIDE SPREAD -->
<section class="spread spread--outside">
  <article class="panel features">
    <div class="features__band"></div>
    <h2 class="heading features__title"><span>Key</span> Features</h2>
    <p class="body-text features__intro">Quillstone is a student success platform built for colleges and universities. It brings advising, early alerts, scheduling and reporting together in one place, so staff can focus on students instead of paperwork. Because it is open source, your campus is never locked in and can shape the tools to fit its own needs.</p>
    <ul class="ticks features__list">
      <li>Open-source software with no license fees</li>
      <li>Advising notes, appointments and early alerts</li>
      <li>Custom reports for registrars and leadership</li>
      <li>Secure hosting on modern cloud hardware</li>
      <li>Custom programming by the people who built it</li>
      <li>Great for schools of all sizes</li>
    </ul>
    <div class="photo" role="img" aria-label="Photo of a man in a suit seen from behind, looking at a city view" style="left:0;bottom:0;width:240px;height:170px;background:linear-gradient(180deg,#c9d3dc 0%,#8fa0b1 55%,#3f4d5c 100%)"></div>
  </article>

  <article class="panel back">
    <svg class="stripes" style="top:0;height:110px" viewBox="0 0 240 110" preserveAspectRatio="none" aria-hidden="true">
      <polygon points="0,0 130,0 0,85" fill="var(--orange)"/>
      <polygon points="130,0 240,0 240,40 60,40" fill="var(--pink)" opacity=".9"/>
      <polygon points="0,85 60,40 240,40 240,70 40,110 0,110" fill="var(--blue)" opacity=".85"/>
    </svg>
    <div class="brand back__brand"><span class="brand__mark"></span>Quillstone</div>
    <p class="body-text back__copy">Quillstone Scholastics hosts, supports and develops Quillstone, the open-source student success system we created. Our team helps advisors, registrars and leaders get more from their data with less cost and less effort. Talk to us about a plan that fits your campus and your budget.</p>
    <div class="back__call">Call us today</div>
    <div class="back__phone"><svg width="15" height="15" viewBox="0 0 24 24" aria-hidden="true"><path fill="var(--pink)" d="M6.6 10.8a15.1 15.1 0 0 0 6.6 6.6l2.2-2.2c.3-.3.7-.4 1-.2 1.1.4 2.3.6 3.6.6.6 0 1 .4 1 1V20c0 .6-.4 1-1 1A17 17 0 0 1 3 4c0-.6.4-1 1-1h3.5c.6 0 1 .4 1 1 0 1.3.2 2.5.6 3.6.1.3 0 .7-.2 1z"/></svg>555-013-4821</div>
    <div class="back__web">www.quillstonescholastics.example</div>
    <svg class="stripes" style="bottom:0;height:70px" viewBox="0 0 240 70" preserveAspectRatio="none" aria-hidden="true">
      <polygon points="0,40 240,10 240,70 0,70" fill="var(--blue)"/>
      <polygon points="0,28 240,0 240,10 0,40" fill="var(--pink)"/>
    </svg>
  </article>

  <article class="panel cover">
    <div class="brand cover__brand"><span class="brand__mark"></span>Quillstone</div>
    <div class="cover__tagline">Scholastics</div>
    <div class="photo" role="img" aria-label="Photo of two colleagues working together at a laptop" style="left:0;top:62px;width:240px;height:250px;background:linear-gradient(135deg,#e7e2dc 0%,#b9a99a 45%,#6f7f90 100%);clip-path:polygon(0 0,100% 0,100% 78%,0 100%)"></div>
    <svg class="stripes" style="top:250px;height:95px" viewBox="0 0 240 95" preserveAspectRatio="none" aria-hidden="true">
      <polygon points="0,62 240,16 240,30 0,76" fill="var(--pink)"/>
      <polygon points="0,76 240,30 240,40 0,86" fill="var(--orange)"/>
      <polygon points="0,86 240,40 240,46 0,92" fill="var(--blue)"/>
    </svg>
    <div class="heading cover__headline">
      <div class="h1">Intuitive and</div>
      <div class="h2">Powerful</div>
      <div class="h3">Affordable Pricing</div>
    </div>
    <div class="cover__bar">www.quillstonescholastics.example</div>
  </article>
</section>

<!-- INSIDE SPREAD -->
<section class="spread spread--inside">
  <article class="panel in-left">
    <div class="brand in-left__brand"><span class="brand__mark"></span>Quillstone</div>
    <div class="photo" role="img" aria-label="Software screenshots shown on a laptop, tablet and phone" style="left:16px;top:40px;width:208px;height:116px;background:linear-gradient(180deg,#f1f4f7,#cfd8e1)"></div>
    <ul class="ticks in-left__list">
      <li>One dashboard for every student record</li>
      <li>Early alerts that reach the right advisor</li>
      <li>Easy scheduling for students and staff</li>
      <li>Flexible reports exported in one click</li>
      <li>Works on desktop, tablet and phone</li>
    </ul>
    <h3 class="heading service__title">Cloud-Based Service</h3>
    <div class="service__sub">Hosting, support and custom development</div>
    <ul class="service__items">
      <li><span class="service__icon" style="background:var(--blue)"></span><div class="body-text"><strong>Hosting</strong>Fast, secure servers with daily backups.</div></li>
      <li><span class="service__icon" style="background:var(--pink)"></span><div class="body-text"><strong>Support</strong>Friendly help from the team who wrote it.</div></li>
      <li><span class="service__icon" style="background:var(--orange)"></span><div class="body-text"><strong>Programming</strong>New features built around your campus.</div></li>
    </ul>
  </article>

  <article class="panel welcome">
    <h2 class="heading welcome__title">Welcome to <span>Quillstone Scholastics</span></h2>
    <div class="body-text welcome__copy">
      <p>We created Quillstone to help colleges keep students on track from their first day to graduation. Today we host and support it for schools across the country.</p>
      <p>Our pricing is a fraction of what larger vendors charge, and because the code is open, your data and your tools always stay yours.</p>
      <p>Whether you serve a few hundred students or many thousands, we will set up, train and support your team every step of the way.</p>
    </div>
    <ul class="ticks welcome__list">
      <li>Lower cost than competing platforms</li>
      <li>No vendor lock-in with open source</li>
      <li>Quick setup and hands-on training</li>
      <li>Built with input from advisors</li>
      <li>Trusted by schools of all sizes</li>
    </ul>
  </article>

  <article class="panel in-right">
    <div class="body-text in-right__copy">
      <p>Every plan includes hosting on state-of-the-art cloud hardware, regular updates and direct access to our developers.</p>
      <p>Need something special? We write custom modules and integrations for your systems.</p>
    </div>
    <div class="photo" role="img" aria-label="Software screenshot of the student dashboard" style="left:18px;top:112px;width:204px;height:140px;background:linear-gradient(180deg,#f4f6f8,#d3dbe3)"></div>
    <ul class="ticks in-right__list">
      <li>Single sign-on and role-based access</li>
      <li>Integrates with your student system</li>
    </ul>
    <div class="photo" role="img" aria-label="Photo of a woman working on a laptop in an office" style="left:0;bottom:0;width:240px;height:190px;background:linear-gradient(160deg,#dfe6ec 0%,#9fb2c2 50%,#55687a 100%)"></div>
  </article>
</section>

</body>
</html>
```